Health Education Non-Profit Needs a Designer to Layout Magazine (Contest)

Hello, we are looking for someone to layout our print magazine. We'd like to work with someone who also has graphic design experience manipulating photos (see 2 sample issue links below for examples). Ad design is also needed. We like the current design of our magazine, so we are hoping our next designer can maintain the same look and feel as our previous magazines. Samples of our past two issues can be found at https://www.harbolwellness.org/wp-content/uploads/2019/03/issue-09-feb-2019.pdf and https://www.harbolwellness.org/wp-content/uploads/2018/11/the-bright-almanac-2018-05-issue-08.pdf

There are typically 2-4 different issues per year with around 11 articles in each issue. Issues are 24 pages. If there is a lot of white space, we may ask the designer to design an ad at the end of the article. We are looking to work with someone who is responsive and has a quick turnaround time (e.g., takes around 3 weeks to design the entire issue).

For this contest, please design a cover and article. Please refer to our last two issues (links above) before designing. We would like to see how the designer can take the images and edit them in a way that incorporates them seamlessly into the magazine as has been done in the past. Our end goal will be for the designer to design the entire issue and future issues. We anticipate this contest will not cover the entire cost of the work for completing the issue. When we find a designer we like, we will work out details for additional payment. Images can be found here: https://files.quorvanshare.net/folders/7KpTzRwq2LmXvNb4Hs9JdYeCa0FgUi3Q?usp=sharing

```html
<!DOCTYPE html>
<html lang="en">
<head>
<meta charset="utf-8">
<title>Dialysis, Caregiving and Emotional Health — Article Spread</title>
<link rel="stylesheet" href="https://fonts.googleapis.com/css2?family=Roboto+Slab:wght@300;800&family=Roboto+Condensed:wght@400;700&display=swap">
<style>
  :root{
    --page:#f3f3f1;
    --ink:#2b2b2b;
    --orange:#e2791d;
    --orange-soft:#f0b07a;
    --rule:#3a3a3a;
    --gutter:#d9d9d6;
  }
  *{box-sizing:border-box;margin:0;padding:0}
  html,body{width:1200px;height:808px;overflow:hidden;background:var(--page)}
  .spread{position:relative;width:1200px;height:808px;background:var(--page);font-family:"Roboto Condensed","Arial Narrow",sans-serif;color:var(--ink);isolation:isolate}
  .gutter{position:absolute;left:592px;top:0;width:24px;height:808px;background:linear-gradient(90deg,transparent,var(--gutter) 50%,transparent)}
  .photo{position:absolute}
  .photo--hero{left:511px;top:0;width:665px;height:418px;background:linear-gradient(100deg,#7d99c4 0%,#c9c7bd 30%,#e6e0d2 50%,#d77a6a 62%,#8aa6c9 85%,#c9a57c 100%)}
  .photo--embrace{left:222px;top:214px;width:277px;height:199px;background:linear-gradient(120deg,#e3e2de 0%,#4f6f5a 45%,#6e7b4a 70%,#d9b2b8 100%)}
  .photo--walk{left:366px;top:515px;width:208px;height:237px;background:linear-gradient(160deg,#8fae70 0%,#5f7f4c 40%,#9db4cf 60%,#3a4f7a 100%)}
  .headline{position:absolute;left:71px;top:26px;width:440px;font-family:"Roboto Slab","Rockwell",Georgia,serif;font-weight:800;color:var(--orange);font-size:54px;line-height:64px;letter-spacing:-1.5px;white-space:nowrap}
  .byline{position:absolute;left:71px;top:214px;width:131px;border-top:2px solid var(--rule);border-bottom:2px solid var(--rule);padding:4px 0 5px;font-family:"Roboto Slab",Georgia,serif;font-weight:300;font-size:14px;letter-spacing:-.3px;white-space:nowrap}
  .body{position:absolute;font-size:7.6px;line-height:10.6px;text-align:justify;hyphens:auto}
  .body p{text-indent:8px}
  .body p.lead,.body p.sub{text-indent:0}
  .body p.sub{margin-top:10.6px}
  .body strong{font-weight:700}
  .dropcap{float:left;font-family:"Roboto Slab",Georgia,serif;font-weight:800;color:var(--orange);font-size:34px;line-height:28px;margin:2px 4px 0 0}
  .col-a{left:71px;top:258px;width:136px;height:496px}
  .col-b{left:218px;top:429px;width:136px;height:325px}
  .pull-quote{position:absolute;left:369px;top:424px;width:215px;font-family:"Roboto Slab",Georgia,serif;font-weight:300;color:var(--orange);font-size:16px;line-height:22px;letter-spacing:-.4px}
  .pull-quote .mark{position:absolute;left:-10px;top:-20px;font-size:78px;line-height:78px;font-weight:800;color:var(--orange-soft);z-index:0}
  .pull-quote .quote-text{position:relative;z-index:1}
  .cols-right{left:633px;top:429px;width:498px;height:326px;column-count:3;column-gap:11px;column-fill:auto}
  .bio{font-style:italic;margin-top:10.6px}
  .bio .arrows{color:var(--orange);font-style:normal;font-weight:700}
  .end-mark{display:inline-block;width:5px;height:5px;background:var(--orange);margin-left:2px}
  .folio{position:absolute;top:766px;border-top:1px solid var(--rule);padding-top:8px;font-size:9px;font-weight:700;display:flex;align-items:center;gap:5px}
  .folio--left{left:71px;width:503px}
  .folio--right{left:633px;width:498px;justify-content:flex-end}
  .folio .sep{color:var(--orange);font-weight:400}
  .brand{font-size:12px;font-weight:700;color:var(--ink);display:flex;align-items:center;gap:3px}
  .brand i{display:inline-block;width:7px;height:7px;border-radius:50%;background:var(--orange)}
</style>
</head>
<body>
<div class="spread">
  <div class="photo photo--hero" role="img" aria-label="Photo: a nurse in blue scrubs talking with an older couple seated on a sofa at home"></div>
  <div class="gutter"></div>

  <h1 class="headline">Dialysis,<br>Caregiving and<br>Emotional Health</h1>
  <div class="byline">By Miriam Oduya</div>

  <div class="photo photo--embrace" role="img" aria-label="Photo: a man leaning over to hug an older woman wrapped in a knitted blanket"></div>

  <div class="body col-a">
    <p class="lead"><span class="dropcap">D</span>ialysis is life-changing in many ways. It may be what makes your life possible, for one. But it may also significantly impact your daily routine, your sense of self and your relationships—and it may impact all three if your significant other or another close relative has taken on a caregiving role.</p>
    <p>You and your caregiver may be new to this situation or coping with it long-term. Either way, psychologists and social workers who work with people with kidney disease and other chronic illnesses can help you both manage your routines, navigate conflicts and maintain—or even enrich—your relationship through this experience.</p>
    <p class="sub"><strong>First, expect a period of adjustment to your new roles.</strong> Immediately following a diagnosis of a chronic disease, patients and caregivers may “focus on logistics—what needs to be taken care of,” says Lena Marsh, PhD, a clinical health psychologist at Alder Lane Counseling in Fairhaven, CO. “The emotional adjustment to the situation doesn’t always set in right away.”</p>
    <p>That may be especially true for people on dialysis. Regardless of whether you’re undergoing it at home or in a treatment center, it involves a great deal of planning, coordination and time. Additionally, caregivers may need to take over new tasks in addition to supporting your treatment regimen.</p>
    <p>All patients face different issues. Dialysis treatments may be a breeze for some, but other may have more challenges. “Some people on dialysis may be limited or fatigued, and some may not be able to pick up the kids from school or perform other role functions,” says Dana Whitcombe, PhD, a transplant psychologist with Westbrook Health in Lakeport. “If they’re unable to work, the caregiver might also be the breadwinner.”</p>
  </div>

  <div class="body col-b">
    <p>You may both struggle during the period of transition until you find what Marsh says her patients often call “the new normal.”</p>
    <p>“Resistance to this huge life change can actually create more distress,” she says. “While it can be a challenging process to get there, being open to and accepting of what’s taking place can be helpful.”</p>
    <p class="sub"><strong>Over the long term, find complementary ways to cope and support each other.</strong> Receiving a kidney transplant is the ultimate goal for many people who experience kidney failure, however, for some patients, dialysis is an indefinite reality. If that’s the case for you, it can be helpful for you and your caregiver to develop ways to collaboratively cope.</p>
    <p>This means viewing the management of your health as a shared responsibility and engaging in joint problem-solving.</p>
    <p>“If there’s a mismatch between the kind of support a patient wants and the kind [he/she is] given, this can cause increased distress,” says Marsh. But, if you work together, you may have better outcomes in your health and in your relationship.</p>
  </div>

  <blockquote class="pull-quote"><span class="mark" aria-hidden="true">”</span><span class="quote-text">The emotional adjustment to the situation doesn’t always set in right away.</span></blockquote>

  <div class="photo photo--walk" role="img" aria-label="Photo: a smiling woman using a walker outdoors beside a young man on a park path"></div>

  <div class="body cols-right">
    <p>If your caregiver is also your spouse or partner, you may have some unique challenges in attaining these good outcomes. “While being married can provide a source of support and solace when one person has a chronic illness, some couples may have pre-existing patterns and interactions in the relationship that aren’t healthy,” Marsh says. A psychologist or other counselor can help you work toward a healthier, more productive dynamic.</p>
    <p class="sub"><strong>Communication is key (and it’s okay if you need help with it).</strong> No matter what your pre-existing relationship is like, you and your caregiver need “open, clear, and quite intimate communication on both sides,” Whitcombe says. Remember that you’re in it together, especially during times of stress or conflict.</p>
    <p>“If there’s a disagreement, the first thing to do is have a conversation and really listen to each other. Try not to blame,” says Whitcombe. “Do a lot of listening and reflecting back: ‘If I heard you correctly, this is what I’m hearing, is that right?’ And then, you can problem-solve effectively as a team.”</p>
    <p>If you’re struggling to do this on your own, psychologists, social workers and other mediators can clarify the problem and identify a resolution. Your psychologist or social worker may be especially helpful if disagreement involves adherence to your prescribed treatment regimen, which is a frequent source of conflict among people on dialysis and their loved ones.</p>
    <p>“If noncompliance is an issue, as a psychologist, I want to know the context,” Whitcombe says. “Aspects of dialysis may be uncomfortable, painful, expensive, inconvenient, or sad, but these things can often be ameliorated. Together, we can all identify the source of the problem, and then find a way to resolve it.”</p>
    <p class="sub"><strong>For caregivers, feeling overwhelmed and having feelings such as guilt or frustration are understandable and normal,</strong> says Marsh.</p>
    <p>“It’s a big change to take on an unexpected role,” she says. “It can be helpful for them to know it is common for caregivers to feel this way. It can also be helpful to encourage them to have open communication to express these feelings.”</p>
    <p>Marsh also suggests that caregivers rely on the medical team, other family members and friends for support. “If the caregiver takes sole responsibility for everything, [he/she will] get burned out,” she cautions.</p>
    <p>Other ways to prevent caregiver burnout include active self-care—like eating well, getting enough sleep and exercising—and keeping a consistent schedule, according to Whitcombe.</p>
    <p>“When your lives are routinized, you know what to expect and there’s less stress of the unknown,” Whitcombe says. “Remember to make time for yourself—and find reasons to laugh.”</p>
    <p>She also suggests that caregivers learn “as much as possible about the medical situation and what dialysis is like, and write it down so you can refer to it when you’re feeling overwhelmed,” she says.</p>
    <p class="sub"><strong>Your relationship may grow even stronger.</strong> You will undoubtedly face both physical and emotional challenges while on dialysis, no matter your prognosis. But patients and caregivers often become deeply bonded, and Whitcombe and Marsh say that you have the opportunity for growth and even joy through this ordeal.</p>
    <p>“These challenging situations can actually bring people closer together,” says Marsh. “Patients and caregivers may experience a shift in values after both evaluating what’s truly important in their lives, they may prioritize things in a new way together.”<span class="end-mark"></span></p>
    <p class="lead bio"><span class="arrows">›››</span> Miriam Oduya is a writer and editor at the National Behavioral Health Society. This resource was developed jointly by the National Behavioral Health Society and Harbol Wellness Education Center as part of a partnership to educate dialysis patients and their families on the psychological and emotional aspects of managing kidney disease.</p>
  </div>

  <div class="folio folio--left">
    <span>48</span><span class="sep">|</span><span>October 2019</span><span class="sep">|</span>
    <span class="brand"><i></i>Bright Almanac</span>
  </div>
  <div class="folio folio--right">
    <span class="brand"><i></i>Bright Almanac</span><span class="sep">|</span><span>October 2019</span><span class="sep">|</span><span>49</span>
  </div>
</div>
</body>
</html>
```